Environmental Consultancy needs new professional Word Template for reporting

A professional looking word template that we can use for all of our reporting.

Word template needs:
- a full scale title page that we can include a different photograph on for each new project, our company logo, title, date, and client details
- Include four layered Headings, table of contents page.
- Each page (except title page) needs to be numbered, with the title of the report at the bottom of the page.
- each page needs our company logo at the top.
- Prefer it to be using similar colours to what we are currently using. Though open to new colours if you come up with something that suits what we do.

Our business is an environment/ecological consultancy and we provide a number of field and reporting based services to mining companies, government agencies, commercial developers, landholders, tourism operators etc. Some of the work we do includes:
- vegetation surveys and reporting
- fauna trapping surveys, and reporting
- water quality and aquatic ecosystem monitoring and reporting
- fish and macroinvertebrate surveys
- seagrass and coral surveys
- environmental impact statements
- environmental offsets
- rehabilitation design and monitoring
- monitoring design programs
- ecological constraints surveys.

I have attached our company logo, a copy of our current title page, and an extract of our current report style (has been greatly reduced and with client information removed). I would like sometime similar to this report style please.

Low design quality

Target Market(s)

Client and Government approval agencies

Industry/Entity Type

Environmental Consultant

Font styles to use
Sans Serif

Colors
faa54b
9bcb3c
00a990
83c9e6
85acd3

Requirements
Must have
• Word template needs:

```html
<!DOCTYPE html>
<html lang="en">
<head>
<meta charset="utf-8">
<title>Receiving Environment Report Template</title>
<link href="https://fonts.googleapis.com/css2?family=Montserrat:wght@400;600;700;800&family=Open+Sans:wght@400;600&display=swap" rel="stylesheet">
<style>
:root{
  --bg:#ffffff;
  --cream:#f4e6c6;
  --cream-dark:#e8d3a6;
  --orange:#faa54b;
  --orange-deep:#e07b1f;
  --brown:#5a3a1e;
  --text:#4a4a4a;
  --muted:#9a8c78;
  --rule:#e2cfa8;
  --green:#9bcb3c;
  --teal:#00a990;
  --sky:#83c9e6;
  --blue:#85acd3;
}
*{margin:0;padding:0;box-sizing:border-box}
html,body{width:839px;height:1200px;overflow:hidden;background:var(--bg)}
body{position:relative;font-family:'Open Sans',sans-serif;color:var(--text)}
.page{position:absolute;background:#fff;box-shadow:0 2px 8px rgba(0,0,0,.18);overflow:hidden}
.cover{left:70px;top:70px;width:699px;height:475px;background:radial-gradient(ellipse at 40% 50%,#fbf0d6 0%,var(--cream) 60%,var(--cream-dark) 100%)}
.cover-map{position:absolute;left:0;top:110px;width:280px;height:300px;background:linear-gradient(160deg,#f7ebcf,#efdcb2);border-radius:40% 45% 35% 50%;opacity:.8}
.cover-photo{position:absolute;left:251px;top:142px;width:448px;height:138px;background:linear-gradient(90deg,#5a1d05 0%,#c4460d 25%,#f59a2a 50%,#fbc45a 60%,#d9621a 80%,#3b1204 100%)}
.brand{position:absolute;display:flex;align-items:center;gap:5px;font-family:'Montserrat',sans-serif;font-weight:600;color:var(--orange-deep)}
.brand .mark{border-radius:50%;background:var(--orange)}
.cover .brand{right:30px;top:84px;font-size:12px}
.cover .brand .mark{width:10px;height:10px}
.cover-title{position:absolute;left:357px;top:290px;font-family:'Montserrat',sans-serif;font-weight:800;color:var(--brown);font-size:32px;line-height:33px;letter-spacing:.3px}
.cover-sub{position:absolute;left:358px;top:360px;font-family:'Montserrat',sans-serif;font-weight:600;font-size:7.5px;color:var(--orange-deep);letter-spacing:.5px}
.cover-client{position:absolute;left:494px;top:382px;border-left:1px solid var(--orange);padding-left:8px;font-family:'Montserrat',sans-serif;color:var(--orange-deep);font-size:9px;line-height:12px}
.cover-client strong{display:block;font-size:14px;line-height:17px;color:var(--brown);font-weight:700}
.spread-page{width:320px;height:240px}
.p1{left:70px;top:600px}.p2{left:449px;top:600px}
.p3{left:70px;top:890px}.p4{left:449px;top:890px}
.running-head{position:absolute;left:16px;top:12px;font-family:'Montserrat',sans-serif;font-size:4.5px;font-weight:600;color:var(--orange);letter-spacing:.5px}
.running-head::after{content:"";display:block;width:120px;height:1px;background:var(--rule);margin-top:3px}
.page-foot{position:absolute;left:16px;bottom:10px;font-size:4px;color:var(--muted)}
.heading{position:absolute;font-family:'Montserrat',sans-serif;font-weight:700;color:var(--orange-deep);font-size:8px;letter-spacing:.4px}
.body{position:absolute;font-size:4px;line-height:6px;color:var(--text)}
.photo{position:absolute;top:0;height:100%}
.photo-sat{left:160px;width:160px;background:linear-gradient(160deg,#dfe7ef 0%,#8aa4bd 30%,#b8773d 60%,#d8a15b 80%,#6f8fae 100%)}
.photo-tree{left:160px;width:160px;background:linear-gradient(180deg,#7fb2dc 0%,#c8b08a 55%,#c56a25 80%,#7a3b12 100%)}
.photo-fire{left:215px;width:105px;background:linear-gradient(180deg,#3b2a1c 0%,#c8631f 50%,#f08a2c 75%,#5a2a10 100%)}
.tab{position:absolute;right:0;top:112px;width:8px;height:14px;background:var(--orange);color:#fff;font-size:6px;line-height:14px;text-align:center}
.p3 .tab,.p1 .tab{right:160px}
.contents{position:absolute;top:36px;font-size:3.8px;line-height:6.2px;width:125px}
.contents .row{display:flex;justify-content:space-between}
.contents .lvl1{font-weight:600;color:var(--orange-deep)}
.contents .lvl2{padding-left:6px}
.chapter-num{position:absolute;left:16px;top:120px;font-family:'Montserrat',sans-serif;font-size:9px;font-weight:700;color:var(--orange-deep)}
</style>
</head>
<body>

<section class="page cover">
  <div class="cover-map" role="img" aria-label="Faint outline map of Australia"></div>
  <div class="brand"><span class="mark"></span>Tallwood Environmental</div>
  <div class="cover-photo" role="img" aria-label="Photograph of kangaroos silhouetted against a sunset"></div>
  <h1 class="cover-title">RECEIVING<br>ENVIRONMENT</h1>
  <p class="cover-sub">MONITORING PROGRAM – FIELD RESULTS REPORT</p>
  <div class="cover-client">Prepared on behalf of<strong>client name</strong>20XX report</div>
</section>

<section class="page spread-page p1">
  <div class="running-head">RECEIVING ENVIRONMENT</div>
  <h2 class="heading" style="left:16px;top:70px">WATER QUALITY<br>FINDINGS</h2>
  <p class="body" style="left:16px;top:96px;width:125px">Field crews sampled each monitoring site across the wet and dry seasons to record water quality, flow and habitat condition. Results were compared against local trigger values and earlier survey rounds to track change over time. Most sites stayed within guideline limits, with short turbidity peaks after heavy rain.</p>
  <p class="body" style="left:16px;top:150px;width:125px">Further detail on methods and site locations is given in the sections that follow.</p>
  <div class="tab">›</div>
  <div class="photo photo-sat" role="img" aria-label="Satellite image of the Australian continent"></div>
  <div class="page-foot">Receiving Environment Report · 2</div>
</section>

<section class="page spread-page p2">
  <div class="running-head">CONTENTS</div>
  <div class="contents" style="left:16px">
    <div class="row lvl1"><span>1 Introduction</span><span>1</span></div>
    <div class="row lvl2"><span>1.1 Background</span><span>1</span></div>
    <div class="row lvl2"><span>1.2 Scope of work</span><span>2</span></div>
    <div class="row lvl2"><span>1.3 Study area</span><span>2</span></div>
    <div class="row lvl1"><span>2 Methods</span><span>3</span></div>
    <div class="row lvl2"><span>2.1 Site selection</span><span>3</span></div>
    <div class="row lvl2"><span>2.2 Water sampling</span><span>4</span></div>
    <div class="row lvl2"><span>2.3 Fauna surveys</span><span>5</span></div>
    <div class="row lvl1"><span>3 Results</span><span>6</span></div>
    <div class="row lvl2"><span>3.1 Water quality</span><span>6</span></div>
    <div class="row lvl2"><span>3.2 Aquatic habitat</span><span>8</span></div>
  </div>
  <div class="contents" style="left:170px">
    <div class="row lvl1"><span>4 Discussion</span><span>10</span></div>
    <div class="row lvl2"><span>4.1 Trends</span><span>10</span></div>
    <div class="row lvl2"><span>4.2 Seasonal change</span><span>11</span></div>
    <div class="row lvl2"><span>4.3 Guideline limits</span><span>12</span></div>
    <div class="row lvl1"><span>5 Recommendations</span><span>13</span></div>
    <div class="row lvl1"><span>6 References</span><span>14</span></div>
    <div class="row lvl1"><span>Appendix A</span><span>15</span></div>
    <div class="row lvl1"><span>Appendix B</span><span>17</span></div>
  </div>
  <div class="tab">›</div>
  <div class="page-foot">Receiving Environment Report · 3</div>
</section>

<section class="page spread-page p3">
  <div class="running-head">RECEIVING ENVIRONMENT</div>
  <div class="chapter-num">1</div>
  <h2 class="heading" style="left:16px;top:134px">INTRODUCTION</h2>
  <p class="body" style="left:16px;top:150px;width:125px">This report presents results from the latest monitoring round of the receiving environment program. It outlines survey aims, site conditions and key findings for the client.</p>
  <div class="tab">›</div>
  <div class="photo photo-tree" role="img" aria-label="Photograph of a lone tree against a blue sky"></div>
  <div class="page-foot">Receiving Environment Report · 4</div>
</section>

<section class="page spread-page p4">
  <div class="running-head">RECEIVING ENVIRONMENT</div>
  <p class="body" style="left:16px;top:36px;width:92px">Monitoring began after approval of the project and continues each year. Sites cover upstream reference creeks and downstream receiving waters. Data are stored in a shared database for review.</p>
  <p class="body" style="left:116px;top:36px;width:92px">Burnt areas were mapped after recent fires to record recovery of ground cover and canopy. Follow up visits will confirm regrowth and any erosion risk near creek lines.</p>
  <div class="photo photo-fire" role="img" aria-label="Photograph of fire crews at a bushfire"></div>
  <div class="page-foot">Receiving Environment Report · 5</div>
</section>

</body>
</html>
```